Delia Morvan
exclusive handcrafted jewelry
Simple
delmorvan@quillbox.net
deliamorvandesign.net
business card should be shaded black like uploaded logo.
I also like the royal blue option !
I have no idea what is on that file since I can not open it . I hope it is my logo in blue or shaded black.

```html
<!DOCTYPE html>
<html lang="en">
<head>
<meta charset="utf-8">
<title>Delia Morvan — Stationery</title>
<link rel="stylesheet" href="https://fonts.googleapis.com/css2?family=Montserrat:wght@300;400&display=swap">
<style>
  :root {
    --bg: #f3f3f3;
    --paper: #ffffff;
    --paper-edge: #dcdcdc;
    --ink: #111111;
    --ink-soft: #555555;
    --black: #0d0d0d;
    --white: #ffffff;
  }
  * { box-sizing: border-box; margin: 0; padding: 0; }
  html, body {
    width: 1200px; height: 727px; overflow: hidden;
    background: var(--bg);
    font-family: "Montserrat", Arial, sans-serif;
    color: var(--ink);
  }
  .canvas { position: relative; width: 1200px; height: 727px; }

  .sheet {
    position: absolute;
    background: var(--paper);
    border: 1px solid var(--paper-edge);
  }

  /* Brand block */
  .brand { display: flex; flex-direction: column; align-items: center; text-align: center; }
  .brand-name { font-weight: 300; letter-spacing: 0.12em; white-space: nowrap; }
  .brand-tag { font-weight: 300; letter-spacing: 0.18em; text-transform: uppercase; color: var(--ink-soft); white-space: nowrap; }

  /* Contact line */
  .contact {
    position: absolute; display: flex; gap: 14px; align-items: center;
    font-weight: 400; color: var(--ink); white-space: nowrap;
  }
  .contact span { display: inline-flex; align-items: center; gap: 4px; }
  .contact svg { width: 8px; height: 8px; fill: currentColor; }

  /* Envelope back */
  .envelope-back { left: 100px; top: 84px; width: 433px; height: 139px; overflow: hidden; }
  .envelope-back .flap { position: absolute; left: 0; top: 0; width: 100%; height: 100px; }
  .envelope-back .brand { position: absolute; left: 0; right: 0; top: 22px; }
  .envelope-back .brand-name { color: var(--white); font-size: 15px; }

  /* Envelope front */
  .envelope-front { left: 163px; top: 260px; width: 461px; height: 196px; }
  .envelope-front .brand { position: absolute; left: 0; right: 0; top: 56px; }
  .envelope-front .brand-name { font-size: 17px; }
  .envelope-front .brand-tag { font-size: 5px; margin-top: 5px; }
  .envelope-front .contact { left: 112px; bottom: 12px; font-size: 6px; }

  /* Business card */
  .business-card {
    left: 526px; top: 370px; width: 184px; height: 117px;
    background: var(--black); border-color: var(--black); color: var(--white);
  }
  .business-card .brand { position: absolute; left: 0; right: 0; top: 30px; }
  .business-card .brand-name { font-size: 12px; }
  .business-card .brand-tag { font-size: 4px; margin-top: 4px; color: #bdbdbd; }
  .business-card .card-web { position: absolute; left: 18px; bottom: 12px; font-size: 5px; font-weight: 300; color: #cfcfcf; letter-spacing: 0.05em; }

  /* Letterhead */
  .letterhead { left: 720px; top: 29px; width: 341px; height: 674px; }
  .letterhead .brand { position: absolute; left: 0; right: 0; top: 36px; }
  .letterhead .brand-name { font-size: 15px; }
  .letterhead .brand-tag { font-size: 4.5px; margin-top: 5px; }
  .letterhead .contact { left: 18px; bottom: 16px; font-size: 5.5px; }
</style>
</head>
<body>
<main class="canvas">

  <section class="sheet envelope-back" aria-label="Envelope back">
    <svg class="flap" viewBox="0 0 433 100" preserveAspectRatio="none" aria-hidden="true">
      <path d="M0 0 H433 V40 Q216 92 0 40 Z" fill="var(--black)"/>
    </svg>
    <div class="brand">
      <p class="brand-name">Delia Morvan</p>
    </div>
  </section>

  <section class="sheet envelope-front" aria-label="Envelope front">
    <div class="brand">
      <p class="brand-name">Delia Morvan</p>
      <p class="brand-tag">exclusive handcrafted jewelry</p>
    </div>
    <div class="contact">
      <span><svg viewBox="0 0 10 10"><path d="M2 0.5 L3.6 2.8 L2.7 3.8 Q3.8 6 6.2 7.3 L7.2 6.4 L9.5 8 L8.3 9.5 Q1 8 0.5 1.7 Z"/></svg>555-014-2270</span>
      <span><svg viewBox="0 0 10 10"><path d="M0.5 2 H9.5 V8 H0.5 Z M1.2 2.6 L5 5.4 L8.8 2.6 V7.4 H1.2 Z" fill-rule="evenodd"/></svg>delmorvan@quillbox.net</span>
      <span><svg viewBox="0 0 10 10"><path d="M5 0.5 A4.5 4.5 0 1 0 5 9.5 A4.5 4.5 0 1 0 5 0.5 Z M5 1.5 A3.5 3.5 0 1 1 5 8.5 A3.5 3.5 0 1 1 5 1.5 Z M1.2 4.5 H8.8 V5.5 H1.2 Z M4.5 1 H5.5 V9 H4.5 Z" fill-rule="evenodd"/></svg>deliamorvandesign.net</span>
    </div>
  </section>

  <section class="sheet business-card" aria-label="Business card">
    <div class="brand">
      <p class="brand-name">Delia Morvan</p>
      <p class="brand-tag">exclusive handcrafted jewelry</p>
    </div>
    <p class="card-web">deliamorvandesign.net</p>
  </section>

  <section class="sheet letterhead" aria-label="Letterhead">
    <div class="brand">
      <p class="brand-name">Delia Morvan</p>
      <p class="brand-tag">exclusive handcrafted jewelry</p>
    </div>
    <div class="contact">
      <span><svg viewBox="0 0 10 10"><path d="M2 0.5 L3.6 2.8 L2.7 3.8 Q3.8 6 6.2 7.3 L7.2 6.4 L9.5 8 L8.3 9.5 Q1 8 0.5 1.7 Z"/></svg>555-014-2270</span>
      <span><svg viewBox="0 0 10 10"><path d="M5 0.5 A4.5 4.5 0 1 0 5 9.5 A4.5 4.5 0 1 0 5 0.5 Z M5 1.5 A3.5 3.5 0 1 1 5 8.5 A3.5 3.5 0 1 1 5 1.5 Z M1.2 4.5 H8.8 V5.5 H1.2 Z M4.5 1 H5.5 V9 H4.5 Z" fill-rule="evenodd"/></svg>deliamorvandesign.net</span>
      <span><svg viewBox="0 0 10 10"><path d="M0.5 2 H9.5 V8 H0.5 Z M1.2 2.6 L5 5.4 L8.8 2.6 V7.4 H1.2 Z" fill-rule="evenodd"/></svg>delmorvan@quillbox.net</span>
    </div>
  </section>

</main>
</body>
</html>
```